Tri-fold Brochure, Postcard & Letterhead Design | ||
Small Engineering Consulting & Services Firm for Building Energy Efficiency | ||
I want to have tri-fold brochure and postcard designs that can represent our company well. Our company is providing engineering consulting and services to improve energy efficiency of building mechanical systems and thus reduce energy consumptions of large commercial buildings. The details of the company information can be found in the website: www.corvalith.com, and any questions about the can be routed to tkal@corvalith.com. I have my company logo and biz card design in different format (originally designed by Emblem Craft Hub) and provide them to designers upon request. | ||
Building owners and facility managers of commercial, institutional and industrial buildings, including large office buildings, hospitals, schools and university campuses, data centers, etc. | ||
The tri-fold brochure and postcard should be designed in a way that its contents can be editable in MS Publisher or Word. The letter head can be designed for use in MS Word. |
HVAC_system_solutions_728.jpg Hello, designers! As posted in our website www.corvalith.com, our company is providing services to improve building energy efficiency. Our customers are building owners, facility managers and operators. The real focus of our business is to optimize the operation of building mechanical systems. We don't do the lighting ourselves and typically oursource the lighting portion. In a building, mechanical systems consume more than 50% of energy for heating, ventilating and air-conditioning. So I would like to have images related to the building mechanical systems. You may google images of "HVAC", "chillers", "AHU", and/or "building automation systems". I will upload some samples from google images. I hope it can help. Thanks, |
CORVALITH_23480_FinalLogo_D4L4_714.jpg Use the uploaded logo and also reference the business card design. To understand the company's services and characters, check out the company website at www.corvalith.com |

```html
<!DOCTYPE html>
<html lang="en">
<head>
<meta charset="utf-8">
<title>Corvalith Stationery Set</title>
<link href="https://fonts.googleapis.com/css2?family=Montserrat:wght@700&family=Open+Sans:wght@400;600&display=swap" rel="stylesheet">
<style>
  :root{
    --brand-blue:#1f6fb8;
    --deep-blue:#0f3f73;
    --pale-blue:#e3edf7;
    --mist-blue:#c9dcef;
    --brand-green:#23956c;
    --ink:#4a4f57;
    --paper:#ffffff;
    --shadow:rgba(0,0,0,.12);
  }
  *{box-sizing:border-box;margin:0;padding:0}
  html,body{width:1200px;height:557px;overflow:hidden;background:var(--paper)}
  body{position:relative;font-family:"Open Sans",Arial,sans-serif;color:var(--ink)}
  .sheet{position:absolute;background:var(--paper);box-shadow:0 1px 4px var(--shadow);overflow:hidden}
  .wordmark{font-family:"Montserrat",Arial,sans-serif;font-weight:700;color:var(--brand-green);letter-spacing:.08em;white-space:nowrap}
  .tagline{font-size:5px;letter-spacing:.12em;color:var(--brand-blue);font-weight:600;white-space:nowrap}

  /* postcard front */
  .postcard-front{left:24px;top:77px;width:228px;height:266px}
  .postcard-front .top-strip{position:absolute;left:0;top:0;width:100%;height:18px;background:var(--deep-blue);color:#fff;font-size:4.6px;font-weight:600;line-height:18px;padding-right:6px;text-align:right;white-space:nowrap}
  .postcard-front .brand{position:absolute;left:8px;top:76px;text-align:center;width:80px}
  .postcard-front .brand .wordmark{font-size:11px}
  .postcard-front .brand .tagline{font-size:4px;margin-top:1px}
  .postcard-front .brand .web{font-size:4.5px;margin-top:4px;color:var(--ink)}
  .postcard-front .hero{position:absolute;left:92px;top:18px;width:136px;height:126px;background:linear-gradient(135deg,#9fc0e0,#3d74ab 60%,#1d4a7c);clip-path:polygon(22% 0,100% 0,100% 100%,0 100%)}
  .postcard-front .band{position:absolute;left:0;top:144px;width:100%;height:122px;background:linear-gradient(160deg,var(--brand-blue),var(--deep-blue))}
  .postcard-front .band .accent{position:absolute;left:0;top:0;width:100%;height:100%;background:var(--mist-blue);clip-path:polygon(0 0,60% 0,0 55%)}
  .postcard-front .thumb{position:absolute;top:26px;width:34px;height:34px;border:1px solid #fff}
  .thumb.t1{left:96px;background:linear-gradient(#b9a48b,#6d5a45)}
  .thumb.t2{left:134px;background:linear-gradient(#8d8f92,#4d5157)}
  .thumb.t3{left:172px;background:linear-gradient(#c7cdd4,#7f8a96)}

  /* postcard back */
  .postcard-back{left:24px;top:360px;width:228px;height:175px}
  .postcard-back .wash{position:absolute;right:0;top:0;width:116px;height:100%;background:linear-gradient(200deg,var(--paper) 10%,var(--pale-blue))}
  .postcard-back .equipment{position:absolute;left:8px;top:10px;width:96px;height:56px;background:linear-gradient(#d8dde3,#8f99a4)}
  .postcard-back .copy{position:absolute;left:8px;top:74px;width:98px;font-size:4.6px;line-height:1.5;color:var(--ink)}
  .postcard-back .divider{position:absolute;left:112px;top:10px;width:1px;height:154px;background:var(--mist-blue)}
  .postcard-back .stamp{position:absolute;right:10px;top:10px;width:26px;height:30px;border:1px solid var(--mist-blue)}
  .postcard-back .address-line{position:absolute;left:124px;width:92px;height:1px;background:var(--mist-blue)}
  .postcard-back .sender{position:absolute;left:118px;top:118px;width:104px;text-align:center}
  .postcard-back .sender .wordmark{font-size:11px}
  .postcard-back .sender .detail{font-size:4.5px;line-height:1.5;margin-top:5px}

  /* letterhead */
  .letterhead{left:283px;top:19px;width:365px;height:528px}
  .letterhead .panel{position:absolute;inset:0;background:linear-gradient(180deg,var(--pale-blue),#edf3fa 60%,var(--pale-blue));clip-path:polygon(58% 0,100% 0,100% 100%,40% 100%,40% 45%)}
  .letterhead .brand{position:absolute;left:24px;top:28px}
  .letterhead .brand .wordmark{font-size:17px}
  .letterhead .contact{position:absolute;left:24px;bottom:26px;font-size:6px;line-height:1.5}

  /* envelope back */
  .envelope-back{left:684px;top:96px;width:504px;height:228px}
  .envelope-back .panel{position:absolute;right:0;top:0;width:200px;height:100%;background:linear-gradient(180deg,var(--pale-blue),#edf3fa);clip-path:polygon(30% 0,100% 0,100% 100%,0 100%)}
  .envelope-back .brand{position:absolute;left:24px;top:20px}
  .envelope-back .brand .wordmark{font-size:12px}
  .envelope-back .return{font-size:6px;line-height:1.5;margin-top:6px}

  /* envelope front */
  .envelope-front{left:684px;top:360px;width:504px;height:156px}
  .envelope-front .flap{position:absolute;left:0;top:0}
  .envelope-front .flap-name{position:absolute;left:0;top:30px;width:100%;text-align:center;color:#fff;font-size:11px}
</style>
</head>
<body>

<section class="sheet postcard-front" aria-label="Postcard front">
  <div class="top-strip">Building Engineering Consulting &amp; Services for Building Energy Efficiency</div>
  <div class="hero" role="img" aria-label="Photo of a modern glass office building in blue tones"></div>
  <div class="brand">
    <div class="wordmark">CORVALITH</div>
    <div class="tagline">ENERGY EFFICIENCY SERVICES</div>
    <div class="web">www.corvalith.com</div>
  </div>
  <div class="band">
    <div class="accent"></div>
    <div class="thumb t1" role="img" aria-label="Photo of building mechanical room"></div>
    <div class="thumb t2" role="img" aria-label="Photo of chiller equipment"></div>
    <div class="thumb t3" role="img" aria-label="Photo of air handling unit"></div>
  </div>
</section>

<section class="sheet postcard-back" aria-label="Postcard back">
  <div class="wash"></div>
  <div class="equipment" role="img" aria-label="Photo of rooftop HVAC units"></div>
  <p class="copy">Corvalith delivers engineering consulting and services that tune building mechanical systems, cut energy use and lower operating costs for owners and facility managers of offices, hospitals, schools, campuses and data centers across the region.</p>
  <div class="divider"></div>
  <div class="stamp"></div>
  <div class="address-line" style="top:62px"></div>
  <div class="address-line" style="top:76px"></div>
  <div class="address-line" style="top:90px"></div>
  <div class="sender">
    <div class="wordmark">CORVALITH</div>
    <div class="detail">1480 Alder Ridge Ct., Halden, OK 73512<br>www.corvalith.com</div>
  </div>
</section>

<section class="sheet letterhead" aria-label="Letterhead">
  <div class="panel"></div>
  <div class="brand">
    <div class="wordmark">CORVALITH</div>
    <div class="tagline">ENERGY EFFICIENCY SERVICES</div>
  </div>
  <div class="contact">1480 Alder Ridge Ct.<br>Halden, OK 73512<br>Phone: 214-555-0147<br>www.corvalith.com</div>
</section>

<section class="sheet envelope-back" aria-label="Envelope return side">
  <div class="panel"></div>
  <div class="brand">
    <div class="wordmark">CORVALITH</div>
    <div class="return">1480 Alder Ridge Ct.<br>Halden, OK 73512</div>
  </div>
</section>

<section class="sheet envelope-front" aria-label="Envelope flap side">
  <svg class="flap" width="504" height="156" viewBox="0 0 504 156" aria-hidden="true">
    <polygon points="0,0 504,0 504,18 252,70 0,18" fill="#1f6fb8"/>
    <polyline points="0,18 252,70 504,18" fill="none" stroke="#0f3f73" stroke-width="1"/>
  </svg>
  <div class="flap-name wordmark">CORVALITH</div>
</section>

</body>
</html>
```